Meridel Capra SA Business Cards

Dear all,
Thank you for reading my brief and project. My company is doing doing advisory in real estate and to comapnies + real estates services as asset management, brokerage, development etc.
I would like to get a business card for my company which is clear, professionnal and serious.
Please have a look to the attachement to see the logos of the company

Industry/Entity Type

Real Estate

Contact Information for Business Card

I would like to have in the business card the following
Principal side:
- Logo of the company (or Monogram)
- First and Last Name (Paulo Vestrand)
- Mobile number
- email address

Second side:
- Address (Chemin des Orvets 17, 1226 Thônex - Switzerland)
- website (www.meridelcapra.ch)

Requirements
Must have
• Refer to the typeface and logo colors

```html
<!DOCTYPE html>
<html lang="en">
<head>
<meta charset="utf-8">
<title>Meridel Capra SA – Business Cards</title>
<link rel="stylesheet" href="https://fonts.googleapis.com/css2?family=Lato:wght@400;700&display=swap">
<style>
  :root {
    --backdrop: #2a2a2a;
    --paper: #ffffff;
    --brand-blue: #0575c2;
    --ink-dark: #3a4350;
    --ink-grey: #555b62;
    --rule-grey: #9a9fa5;
    --rule-light: #8fc0e6;
  }
  * { box-sizing: border-box; margin: 0; padding: 0; }
  html, body {
    width: 1200px; height: 1200px; overflow: hidden;
    background: var(--backdrop);
    font-family: "Lato", sans-serif;
  }
  .card {
    position: absolute; top: 310px; height: 594px;
    box-shadow: 2px 3px 6px rgba(0,0,0,.45);
    text-align: center;
  }
  .card--front { left: 234px; width: 364px; background: var(--paper); }
  .card--back  { left: 627px; width: 369px; background: var(--brand-blue); color: var(--paper); }

  .brand-dot {
    position: absolute; left: 50%; top: 92px; width: 90px; height: 90px;
    margin-left: -45px; border-radius: 50%; background: var(--brand-blue);
  }
  .brand-name {
    position: absolute; left: 0; right: 0; top: 226px;
    font-size: 33px; font-weight: 700; letter-spacing: .5px; color: var(--ink-dark);
  }
  .holder-name {
    position: absolute; left: 0; right: 0; top: 400px;
    font-size: 23px; letter-spacing: .2px; color: var(--ink-dark);
  }
  .holder-name .first { font-weight: 700; }
  .holder-name .last { color: var(--brand-blue); }
  .contact-icons { position: absolute; left: 87px; top: 444px; }
  .contact-list {
    position: absolute; left: 0; right: 0; top: 480px;
    font-size: 17px; line-height: 22px; color: var(--ink-grey);
  }
  .contact-list .accent { color: var(--brand-blue); }

  .back-mark {
    position: absolute; left: 50%; top: 110px; width: 170px; height: 170px;
    margin-left: -85px; border-radius: 50%; background: var(--paper);
  }
  .back-name {
    position: absolute; left: 0; right: 0; top: 316px;
    font-size: 30px; font-weight: 700; letter-spacing: .5px;
  }
  .address {
    position: absolute; left: 0; right: 0; top: 432px;
    font-size: 17px; line-height: 21.5px; font-style: normal;
  }
  .back-rule {
    position: absolute; left: 87px; width: 195px; top: 514px;
    border-top: 1px solid var(--rule-light);
  }
  .website {
    position: absolute; left: 0; right: 0; top: 525px; font-size: 20px;
  }
</style>
</head>
<body>
  <section class="card card--front">
    <div class="brand-dot"></div>
    <div class="brand-name">MERIDEL CAPRA</div>
    <div class="holder-name"><span class="first">PAULO</span> <span class="last">VESTRAND</span></div>
    <svg class="contact-icons" width="190" height="26" viewBox="0 0 190 26">
      <line x1="0" y1="13" x2="54" y2="13" stroke="var(--rule-grey)" stroke-width="1"/>
      <line x1="136" y1="13" x2="190" y2="13" stroke="var(--rule-grey)" stroke-width="1"/>
      <circle cx="67" cy="13" r="12" fill="var(--brand-blue)"/>
      <circle cx="95" cy="13" r="12" fill="var(--brand-blue)"/>
      <circle cx="123" cy="13" r="12" fill="var(--brand-blue)"/>
      <!-- phone -->
      <path d="M60 12 q7 -6 14 0 l-1.5 2 h-2 v-1.5 h-7 v1.5 h-2 z M62 15 h10 v4 h-10 z" fill="#fff"/>
      <!-- envelope -->
      <rect x="88.5" y="8.5" width="13" height="9" fill="none" stroke="#fff" stroke-width="1.5"/>
      <path d="M88.5 8.5 l6.5 5 l6.5 -5" fill="none" stroke="#fff" stroke-width="1.5"/>
      <!-- globe -->
      <circle cx="123" cy="13" r="6.5" fill="none" stroke="#fff" stroke-width="1.5"/>
      <path d="M116.5 13 h13 M123 6.5 q-4 6.5 0 13 q4 -6.5 0 -13" fill="none" stroke="#fff" stroke-width="1.2"/>
    </svg>
    <div class="contact-list">
      <div>044-870 315 264</div>
      <div>info@meridelcapra.ch</div>
      <div>www.<span class="accent">meridelcapra</span>.ch</div>
    </div>
  </section>

  <section class="card card--back">
    <div class="back-mark"></div>
    <div class="back-name">MERIDEL CAPRA</div>
    <address class="address">
      Chemin des Orvets 17,<br>
      1226 Thônex<br>
      Switzerland
    </address>
    <div class="back-rule"></div>
    <div class="website">www.meridelcapra.ch</div>
  </section>
</body>
</html>
```